Business Card Design Project

Use newly designed logo and tie into newly designed website
I need a new logo and website layout designed for my partner's business. This is a birthday present. His business is interior painting, wallpapering and design. He also has access to a wide variety of products including carpet, fabrics, furniture, wallpaper, tile, countertops, etc. I have attached some screen shots of his website for reference. He is a one man shop and has a stellar reputation with his customers. He is on-time, very tidy, excellent with animals, and always finishes on time and on budget. There are no restrictions on colors or fonts. The logo needs to work well with the website, business cards and printed materials. The website needs to flow content for device size so it looks just as good on a cell phone or tablet as it does on a desktop computer. Whatever the heck that's called!Thanks. I am looking forward to seeing everyone's ideas.
Target Market(s)
Consumers looking to improve the interior environment of their homes by updating wall paint or paper, flooring (either carpet, tile, or hardwoods), counter tops, window treatments, etc. Clients tend to be more upper middle class and have certain taste levels and expectations. New logo, website and business card should align to meet those levels.
Industry/Entity Type
Cell Phone
Look and feel

```html
<!DOCTYPE html>
<html lang="en">
<head>
<meta charset="utf-8">
<title>Verrano Interior Designs – Business Card</title>
<link rel="stylesheet" href="https://fonts.googleapis.com/css2?family=Cinzel:wght@500;600&display=swap">
<style>
  :root {
    --navy: #140d33;
    --gold: #9c855a;
    --brick: #8b1c1f;
    --amber: #f59d0e;
    --white: #ffffff;
    --page: #e6e4e0;
  }
  html, body {
    margin: 0;
    width: 1200px;
    height: 1000px;
    overflow: hidden;
    background: var(--page);
  }
  .card {
    position: absolute;
    left: 100px;
    top: 214px;
    width: 1000px;
    height: 572px;
    background: var(--white);
    box-shadow: 0 6px 24px rgba(0,0,0,.18);
    overflow: hidden;
    font-family: "Cinzel", "Trajan Pro", serif;
  }
  .card__panel {
    position: absolute;
    left: 170px;
    top: 300px;
    right: 0;
    bottom: 0;
    background: var(--navy);
  }
  .brand {
    position: absolute;
    left: 190px;
    top: 60px;
    display: flex;
    align-items: center;
    gap: 34px;
  }
  .brand__square {
    width: 190px;
    height: 190px;
    background: var(--brick);
    flex: none;
  }
  .brand__name {
    color: var(--navy);
    font-weight: 600;
    line-height: 1;
    margin: 0;
  }
  .brand__primary {
    display: block;
    font-size: 92px;
    letter-spacing: 2px;
  }
  .brand__secondary {
    display: block;
    font-size: 40px;
    letter-spacing: 1px;
    margin-top: 6px;
  }
  .contact {
    position: absolute;
    left: 380px;
    top: 328px;
    color: var(--white);
    font-weight: 500;
  }
  .contact__name {
    font-size: 42px;
    margin: 0 0 8px;
    font-weight: 600;
    letter-spacing: 1px;
  }
  .contact__list {
    list-style: none;
    margin: 0;
    padding: 0;
  }
  .contact__item {
    display: flex;
    align-items: center;
    gap: 12px;
    font-size: 22px;
    line-height: 1.45;
  }
  .contact__item--phone {
    font-size: 36px;
    line-height: 1.3;
  }
  .contact__icon {
    width: 20px;
    height: 20px;
    fill: var(--amber);
    flex: none;
  }
</style>
</head>
<body>
  <div class="card">
    <div class="card__panel"></div>

    <div class="brand">
      <div class="brand__square"></div>
      <h1 class="brand__name">
        <span class="brand__primary">VERRANO</span>
        <span class="brand__secondary">INTERIOR DESIGNS</span>
      </h1>
    </div>

    <div class="contact">
      <p class="contact__name">DANA VERRANO</p>
      <ul class="contact__list">
        <li class="contact__item contact__item--phone">
          <svg class="contact__icon" viewBox="0 0 20 20" aria-hidden="true"><path d="M5 2l3 3-2 2c1 2.5 3 4.5 5.5 5.5l2-2 3 3-2 3C8 16 4 12 2 5z"/></svg>
          913-555-0148
        </li>
        <li class="contact__item">
          <svg class="contact__icon" viewBox="0 0 20 20" aria-hidden="true"><path d="M2 5h16v10H2z M2 5l8 6 8-6" stroke="#140d33" stroke-width="1.2"/></svg>
          DANA@VERRANODESIGNS.COM
        </li>
        <li class="contact__item">
          <svg class="contact__icon" viewBox="0 0 20 20" aria-hidden="true"><circle cx="10" cy="10" r="8"/><path d="M2 10h16M10 2c-4 4-4 12 0 16M10 2c4 4 4 12 0 16" stroke="#140d33" stroke-width="1.2" fill="none"/></svg>
          WWW.VERRANODESIGNS.COM
        </li>
        <li class="contact__item">
          <svg class="contact__icon" viewBox="0 0 20 20" aria-hidden="true"><path d="M10 2l8 7h-2v9h-4v-5H8v5H4V9H2z"/></svg>
          2207 W LINDEN CT • MAPLE HILL, KS 66099
        </li>
      </ul>
    </div>
  </div>
</body>
</html>
```